Business Card Design

I need a business card designed for my business.

The company name is Miles Renford Collective

It has four brands underneath it. They are:
- MR Occasions
- MR Athletic Journeys
- MRC Stewardship
- Dove Draftworks

I have attached all logo items, as well as our last business card.

I look forward to seeing your designs.

Industry/Entity Type

Business

Colors
eb1f27
0355a3

Requirements
Must have
• Our contact details as per the front page of our previous business card.

```html
<!DOCTYPE html>
<html lang="en">
<head>
<meta charset="utf-8">
<title>Miles Renford Collective – Business Card</title>
<link rel="stylesheet" href="https://fonts.googleapis.com/css2?family=Open+Sans:wght@400;600;700&display=swap">
<style>
  :root {
    --brand-blue: #0355a3;
    --brand-blue-light: #2f86d6;
    --brand-blue-deep: #023f7c;
    --brand-red: #eb1f27;
    --ink-grey: #5b6470;
    --paper: #ffffff;
    --paper-shade: #eef1f5;
    --backdrop: #e4e6ea;
  }
  * { box-sizing: border-box; margin: 0; padding: 0; }
  html, body { width: 1200px; height: 934px; overflow: hidden; }
  body {
    background: var(--backdrop);
    font-family: "Open Sans", Arial, sans-serif;
    position: relative;
  }
  .card {
    position: absolute;
    top: 300px;
    width: 520px;
    height: 318px;
    border-radius: 6px;
    overflow: hidden;
    box-shadow: 0 10px 28px rgba(0, 0, 0, 0.18);
  }

  /* Front face */
  .card-front {
    left: 50px;
    background: linear-gradient(135deg, var(--paper) 55%, var(--paper-shade));
  }
  .edge-bands {
    position: absolute; top: 0; right: 0; bottom: 0;
    display: flex;
  }
  .edge-band-red { width: 8px; background: var(--brand-red); }
  .edge-band-gap { width: 6px; background: var(--paper); }
  .edge-band-blue {
    width: 56px;
    background: linear-gradient(180deg, var(--brand-blue-light), var(--brand-blue) 55%, var(--brand-blue-deep));
  }
  .front-logo {
    position: absolute; left: 40px; top: 30px;
    display: flex; align-items: center; gap: 10px;
  }
  .logo-dot {
    width: 34px; height: 34px; border-radius: 50%;
    background: var(--brand-blue);
    flex: none;
  }
  .logo-name {
    font-weight: 700; font-size: 19px; color: var(--brand-blue);
    line-height: 1.05; text-transform: uppercase; letter-spacing: 0.5px;
  }
  .holder { position: absolute; left: 40px; top: 96px; }
  .holder-name { font-size: 22px; font-weight: 700; color: var(--brand-blue); }
  .holder-role {
    font-size: 12px; letter-spacing: 5px; color: var(--ink-grey);
    margin-top: 2px;
  }
  .contact-list {
    position: absolute; left: 40px; top: 172px;
    list-style: none;
    display: grid; grid-template-columns: auto auto; column-gap: 26px; row-gap: 12px;
    font-size: 11.5px; color: var(--ink-grey);
  }
  .contact-list li { display: flex; align-items: center; gap: 7px; }
  .contact-list li.full { grid-column: 1 / span 2; }
  .contact-icon { width: 14px; height: 14px; flex: none; fill: var(--brand-blue); }

  /* Back face */
  .card-back {
    left: 630px;
    background: linear-gradient(160deg, var(--brand-blue-light) 0%, var(--brand-blue) 50%, var(--brand-blue-deep) 100%);
  }
  .back-logo {
    position: absolute; left: 150px; top: 60px;
    display: flex; align-items: center; gap: 12px;
  }
  .back-logo .logo-dot { background: var(--paper); width: 40px; height: 40px; }
  .back-logo .logo-name { color: var(--paper); font-size: 22px; }
  .tagline {
    position: absolute; left: 202px; top: 126px;
    font-size: 12px; color: var(--paper); letter-spacing: 0.3px;
  }
  .brand-band {
    position: absolute; left: 0; right: 0; top: 170px; height: 62px;
    background: var(--paper);
    display: flex; justify-content: space-around; align-items: center;
    padding: 0 14px;
  }
  .brand-name { font-size: 12px; font-weight: 700; text-align: center; line-height: 1.15; }
  .brand-events { color: var(--brand-blue); }
  .brand-sports { color: var(--brand-red); }
  .brand-management { color: var(--brand-blue); }
  .brand-kreative { color: var(--brand-red); }
</style>
</head>
<body>

<section class="card card-front" aria-label="Business card front">
  <div class="edge-bands" aria-hidden="true">
    <span class="edge-band-red"></span>
    <span class="edge-band-gap"></span>
    <span class="edge-band-blue"></span>
  </div>

  <div class="front-logo">
    <span class="logo-dot"></span>
    <span class="logo-name">Miles Renford<br>Collective</span>
  </div>

  <div class="holder">
    <p class="holder-name">Owen Hartley</p>
    <p class="holder-role">PRINCIPAL</p>
  </div>

  <ul class="contact-list">
    <li class="full">PO Box 418 Belmont ACT 2609 Australia</li>
    <li>
      <svg class="contact-icon" viewBox="0 0 24 24" aria-hidden="true"><path d="M6.6 10.8a15.1 15.1 0 0 0 6.6 6.6l2.2-2.2c.3-.3.7-.4 1-.2 1.1.4 2.3.6 3.6.6.6 0 1 .4 1 1V20c0 .6-.4 1-1 1A17 17 0 0 1 3 4c0-.6.4-1 1-1h3.5c.6 0 1 .4 1 1 0 1.3.2 2.5.6 3.6.1.3 0 .7-.2 1z"/></svg>
      +61 2 5550 1842
    </li>
    <li>
      <svg class="contact-icon" viewBox="0 0 24 24" aria-hidden="true"><path d="M2 5h20v14H2z M3.5 6.5l8.5 6 8.5-6" fill="none" stroke="var(--brand-blue)" stroke-width="2"/></svg>
      owen@MilesRenford.com.au
    </li>
    <li>
      <svg class="contact-icon" viewBox="0 0 24 24" aria-hidden="true"><path d="M6.6 10.8a15.1 15.1 0 0 0 6.6 6.6l2.2-2.2c.3-.3.7-.4 1-.2 1.1.4 2.3.6 3.6.6.6 0 1 .4 1 1V20c0 .6-.4 1-1 1A17 17 0 0 1 3 4c0-.6.4-1 1-1h3.5c.6 0 1 .4 1 1 0 1.3.2 2.5.6 3.6.1.3 0 .7-.2 1z"/></svg>
      +61 400 555 318
    </li>
    <li>
      <svg class="contact-icon" viewBox="0 0 24 24" aria-hidden="true"><g fill="none" stroke="var(--brand-blue)" stroke-width="2"><circle cx="12" cy="12" r="9"/><path d="M3 12h18M12 3c3 3 3 15 0 18M12 3c-3 3-3 15 0 18"/></g></svg>
      www.MilesRenford.com.au
    </li>
  </ul>
</section>

<section class="card card-back" aria-label="Business card back">
  <div class="back-logo">
    <span class="logo-dot"></span>
    <span class="logo-name">Miles Renford<br>Collective</span>
  </div>
  <p class="tagline">Event, Travel And Talent Management</p>

  <div class="brand-band">
    <span class="brand-name brand-events">MR<br>Occasions</span>
    <span class="brand-name brand-sports">MR Athletic<br>Journeys</span>
    <span class="brand-name brand-management">MRC<br>Stewardship</span>
    <span class="brand-name brand-kreative">Dove<br>Draftworks</span>
  </div>
</section>

</body>
</html>
```